TRELOS - Web Design Project

Task Description
RELOS is the major VANTRA project supporting the Indonesian Bureau of Tidal Works and Harvests (BTWH). BTWH is responsible for promoting sustainable use of fish and other marine resources for Indonesia’s long-term economic prosperity. Its mandate encompasses such issues as drafting of marine and fisheries sector policies; control of overfishing, destructive and illegal fishing practices; spatial planning for resource use; management of conservation areas; data analysis and modeling for fisheries management; and promoting the long-term welfare of fishing communities. The TRELOS project is supporting BTWH efforts to achieve sustainability in the marine and fisheries sector and to improve the response of coastal communities to near-term disasters and long-term impacts related to climate change.

The TRELOS project has three key thematic areas: [policy] [1], [sustainable fisheries] [2], and [climate change] [3] — as well as supporting overall coordination of [Ocean Stewardship Scheme] [4] activities.
Updates

Reason: There are two public holidays in Indonesia so we are unable to provide feedback to designers between 17th and the 20th.

a few people have asked for reference sites - there is really no reference site we can give but I have attached a jpg for some ideas - we are after innovated ideas that will capture people's attention but which is extermely easy to use and navigate. 

the main focus should be on a map on Indonesia with focal points of our three offices (and with great navigation buttons/tools). 

please give us something amazing and use your design skills to make an amazing site

thanks

Target Market(s)

under 25, college or uni - research students - others interested in marine and fisheries

Industry/Entity Type

Sustainability

Requirements
Must have
• The web must have Indonesia map on the center with button on Jakarta city as headquarter, Sulawesi Tenggara (Wakatobi) as branch office and Nusa Tenggara Barat (Mataram), must have an icon for navigation on the upper, left or bottom side. Example of layout is attached (only as example). The "buttons" should then be used as navigation tools

We are after innovative ideas that with easy navigation features.

Current website is www.trelosventure.example - this is seen as too hard to navigate

Navigation Icons will also need to be developed;
- About
- Activities
- News
Library
Press releases
Publications
- Partners
- Links

site will also need to adhere to these the VANTRA branding guidelines
http://www.vantra.example/branding/VANTRA_Graphic_Standards_Manual.pdf

TRELOS Logo is attached

Nice to have
• - based on scaffold plinkora, site will be hosted on fenwixo7 platform. (http://plinkora.codehub.example/)

```html
<!DOCTYPE html>
<html lang="en">
<head>
<meta charset="utf-8">
<title>TRELOS Project</title>
<link href="https://fonts.googleapis.com/css2?family=PT+Sans:wght@400;700&family=Arimo:wght@400&display=swap" rel="stylesheet">
<style>
:root{
  --page:#ffffff;
  --header-top:#ffffff;
  --header-bottom:#ececec;
  --band:#e9e9e9;
  --panel:#ffffff;
  --line:#e2e2e2;
  --heading:#6e6e6e;
  --text:#8c8c8c;
  --nav-text:#6a6a6a;
  --link:#1e5a9e;
  --icon:#3d8fd6;
  --icon-light:#8cc3ef;
  --pin-red:#d9342b;
  --pin-blue:#2f8fe0;
  --footer-text:#8a8a8a;
  --map-a:#f4f4f4;
  --map-b:#dcdcdc;
}
*{box-sizing:border-box;margin:0;padding:0}
html,body{width:1200px;height:701px;overflow:hidden;background:var(--page)}
body{position:relative;font-family:"PT Sans",sans-serif}

.site-header{position:absolute;left:0;top:0;width:1200px;height:104px;
  background:linear-gradient(var(--header-top),var(--header-bottom));border-bottom:1px solid #dcdcdc}
.brand-name{position:absolute;left:62px;top:30px;font-weight:700;font-size:28px;color:var(--heading);letter-spacing:.5px}
.search{position:absolute;left:944px;top:42px;display:flex}
.search-field{width:174px;height:30px;border:1px solid #cfcfcf;border-radius:3px 0 0 3px;background:#fff;
  font-family:"Arimo",sans-serif;font-size:13px;color:#b9b9b9;padding:7px 14px}
.search-button{width:33px;height:30px;border-radius:0 3px 3px 0;background:linear-gradient(#6fb0ec,#3a83cf);
  display:flex;align-items:center;justify-content:center}

.main-band{position:absolute;left:12px;top:105px;width:1176px;height:492px;background:var(--band)}
.card{position:absolute;z-index:2;top:120px;height:489px;background:var(--panel);box-shadow:0 0 6px rgba(0,0,0,.12)}
.nav-card{left:57px;width:223px;border-radius:4px 0 0 4px}
.content-card{left:838px;width:310px;border-radius:0 4px 4px 0}
.card-heading{height:48px;border-bottom:1px solid var(--line);font-weight:700;font-size:17px;color:var(--heading);
  padding:14px 0 0 23px}
.content-card .card-heading{padding-left:35px}

.nav-list{list-style:none;padding-top:14px}
.nav-item{height:47.5px;display:flex;align-items:center;padding-left:19px;gap:12px;font-size:15.5px;color:var(--nav-text)}
.nav-icon{width:29px;height:29px;border-radius:4px;background:linear-gradient(var(--icon-light),var(--icon));
  border:2px solid #e3eef8;display:flex;align-items:center;justify-content:center}
.nav-icon.muted{background:linear-gradient(#d0d0d0,#a6a6a6);border-color:#eee}

.map-panel{position:absolute;z-index:2;left:280px;top:120px;width:557px;height:489px;border:1px solid #d6d6d6;
  background:repeating-linear-gradient(#f6f6f6 0 2px,#ececec 2px 3px)}
.map-fill{position:absolute;left:2px;top:120px;width:553px;height:280px;
  background:radial-gradient(ellipse at 50% 55%,var(--map-b),var(--map-a) 75%,transparent)}
.tag{position:absolute;height:26px;border-radius:3px;background:linear-gradient(#808080,#5c5c5c);
  color:#fff;font-weight:700;font-size:12.5px;line-height:26px;text-align:center;box-shadow:0 1px 2px rgba(0,0,0,.35)}
.tag::after{content:"";position:absolute;left:50%;bottom:-6px;margin-left:-6px;border:6px solid transparent;border-bottom:0;border-top-color:#5c5c5c}
.pin{position:absolute;width:16px;height:28px}
.legend{position:absolute;left:15px;bottom:14px;display:flex;gap:18px;font-size:12.5px}
.legend-item{display:flex;align-items:center;gap:7px}
.legend-dot{width:13px;height:13px;border-radius:50%}
.legend-item.hq{color:var(--link)}
.legend-item.branch{color:#9a9a9a}

.content-body{padding:16px 26px 0 36px;font-size:12.3px;line-height:23.5px;color:var(--text);text-align:justify}
.view-more{position:absolute;right:30px;top:426px;font-weight:700;font-size:12.5px;color:var(--link)}

.site-footer{position:absolute;z-index:1;left:0;top:597px;width:1200px;height:104px;background:linear-gradient(#f4f4f4,#ececec);
  font-family:"Arimo",sans-serif;font-size:13px;color:var(--footer-text)}
.legal{position:absolute;left:53px;top:29px;line-height:21px}
.footer-links{position:absolute;right:47px;top:28px}
.footer-links span{margin:0 9px}
</style>
</head>
<body>
<header class="site-header">
  <div class="brand-name">VANTRA</div>
  <div class="search">
    <div class="search-field">Search something...</div>
    <div class="search-button"><svg width="14" height="14" viewBox="0 0 14 14"><circle cx="6" cy="6" r="4" fill="none" stroke="#fff" stroke-width="2"/><path d="M9 9l4 4" stroke="#fff" stroke-width="2.4"/></svg></div>
  </div>
</header>

<div class="main-band"></div>

<nav class="card nav-card">
  <h2 class="card-heading">NEVIGATIONS</h2>
  <ul class="nav-list">
    <li class="nav-item"><span class="nav-icon muted"><svg width="15" height="15" viewBox="0 0 16 16"><circle cx="8" cy="8" r="5" fill="none" stroke="#fff" stroke-width="3" stroke-dasharray="2.5 1.5"/></svg></span>ABOUT US</li>
    <li class="nav-item"><span class="nav-icon"><svg width="15" height="13" viewBox="0 0 15 13"><path d="M1 4h4l7-3v11l-7-3H1z" fill="#fff"/></svg></span>ACTIVITIES</li>
    <li class="nav-item"><span class="nav-icon"><svg width="11" height="15" viewBox="0 0 11 15"><rect x="3" y="0" width="5" height="9" rx="2.5" fill="#fff"/><path d="M1 7a4.5 4.5 0 009 0M5.5 12v3" stroke="#fff" fill="none" stroke-width="1.5"/></svg></span>NEWS</li>
    <li class="nav-item"><span class="nav-icon"><svg width="15" height="13" viewBox="0 0 15 13"><path d="M1 1h6v11H1zM8 1h6v11H8z" fill="#fff"/></svg></span>LIBRARY</li>
    <li class="nav-item"><span class="nav-icon"><svg width="14" height="14" viewBox="0 0 14 14"><rect x="1" y="1" width="10" height="12" fill="#fff"/><path d="M6 10l7-7" stroke="#2a6fb6" stroke-width="2"/></svg></span>PRESS RELEASE</li>
    <li class="nav-item"><span class="nav-icon"><svg width="15" height="13" viewBox="0 0 15 13"><rect x="1" y="3" width="13" height="9" rx="1" fill="#fff"/><rect x="5" y="0.5" width="5" height="3" fill="none" stroke="#fff"/></svg></span>PUBLICATIONS</li>
    <li class="nav-item"><span class="nav-icon"><svg width="15" height="13" viewBox="0 0 15 13"><circle cx="5" cy="4" r="2.5" fill="#fff"/><circle cx="10.5" cy="4" r="2.5" fill="#fff"/><path d="M0.5 12c0-4 9-4 9 0zM7 12c0-4 7.5-4 7.5 0z" fill="#fff"/></svg></span>PARTNERS</li>
    <li class="nav-item"><span class="nav-icon"><svg width="7" height="15" viewBox="0 0 7 15"><circle cx="4" cy="2" r="2" fill="#fff"/><path d="M2 6h3v9H2z" fill="#fff"/></svg></span>LINKS</li>
  </ul>
</nav>

<section class="map-panel">
  <div class="map-fill" role="img" aria-label="Grey map of the Indonesian archipelago"></div>
  <div class="tag" style="left:190px;top:88px;width:143px">SULAWESI TENGGARA</div>
  <svg class="pin" style="left:254px;top:126px" viewBox="0 0 16 28"><path d="M7 12h2v15H7z" fill="#555"/><circle cx="8" cy="7" r="6.5" fill="var(--pin-red)"/><circle cx="6" cy="5" r="2" fill="#f8a19b"/></svg>
  <div class="tag" style="left:151px;top:280px;width:77px">JAKARTA</div>
  <svg class="pin" style="left:178px;top:316px" viewBox="0 0 16 28"><path d="M7 12h2v15H7z" fill="#555"/><circle cx="8" cy="7" r="6.5" fill="var(--pin-blue)"/><circle cx="6" cy="5" r="2" fill="#a8d4f7"/></svg>
  <div class="tag" style="left:229px;top:328px;width:157px">NUSA TENGGARA BARAT</div>
  <svg class="pin" style="left:307px;top:364px" viewBox="0 0 16 28"><path d="M7 12h2v15H7z" fill="#555"/><circle cx="8" cy="7" r="6.5" fill="var(--pin-red)"/><circle cx="6" cy="5" r="2" fill="#f8a19b"/></svg>
  <div class="legend">
    <span class="legend-item hq"><span class="legend-dot" style="background:var(--pin-blue)"></span>HEADQUARTES</span>
    <span class="legend-item branch"><span class="legend-dot" style="background:var(--pin-red)"></span>BRANCH OFFICE</span>
  </div>
</section>

<section class="card content-card">
  <h2 class="card-heading">CONTENT HEADING HERE</h2>
  <p class="content-body">Lorem ipsum dolor sit ipusmLorem ipsum dolor sit ipusmLorem ipsum dolor sit ipusmLorem ipsum dolor sit ipusmLorem ipsum dolor sit ipusmLorem ipsum dolor sit ipusmLorem ipsum dolor sit ipusmLorem ipsum dolor sit ipusmLorem ipsum dolor sit ipusmLorem ipsum dolor sit ipusmLorem ipsum dolor sit ipusmLorem ipsum dolor sit ipusmLorem ipsum dolor sit ipusmLorem ipsum dolor sit ipusmLorem ipsum dolor sit ipusmLorem ipsum dolor sit ipusmLorem ipsum dolor sit ipusmLorem ipsum dolor sit ipusmLorem ipsum dolor sit ipusmLorem ipsum dolor sit ipusmLorem ipsum dolor sit ipusmLorem ipsum dolor sit ipu.</p>
  <span class="view-more">VIEW MORE...</span>
</section>

<footer class="site-footer">
  <p class="legal">Copyright © 2012-2014 Halvern Global Inc. TRELOS - Privacy policy<br>The information provided on this website is not official Sponsoring Government information and does not represent the views<br>or positions of the Agency for Overseas Partnerships or the Sponsoring Government.</p>
  <p class="footer-links">Home<span>|</span>About Us<span>|</span>Our Activities<span>|</span>Contact Us</p>
</footer>
</body>
</html>
```